Consulting company needs Business Cards - rough concept provided

I'm looking for someone to take our business card idea and make is slick and polished - to communicate our high-end, sophisticated, serious consulting business. We have a rough layout we did in-house. We are open to ideas on repo-ing elements, adjusting sizes, typefaces etc... within the general concept we've already come up with. We want it to be super-clean and sophisticated. We want to keep the white backgrounds, and blue brand colors. Our goal is to print with painted blue edges on thick cardstock. Thank you!!

```html
<!DOCTYPE html>
<html lang="en">
<head>
<meta charset="utf-8">
<title>Northvale Business Cards</title>
<link href="https://fonts.googleapis.com/css2?family=Montserrat:wght@700&family=Jost:wght@400&display=swap" rel="stylesheet">
<style>
  :root {
    --brand-blue: #0399d9;
    --paper: #ffffff;
    --ink: #333333;
    --muted: #5a5a5a;
    --ghost-on-blue: rgba(0, 80, 140, 0.12);
    --ghost-on-white: #f3f4f5;
    --backdrop: #dcdcdc;
  }
  html, body {
    margin: 0;
    width: 1200px;
    height: 900px;
    overflow: hidden;
    background: var(--backdrop);
  }
  .sheet {
    position: relative;
    width: 1200px;
    height: 900px;
  }
  .card {
    position: absolute;
    left: 260px;
    width: 680px;
    height: 388px;
    border-radius: 34px;
    overflow: hidden;
    box-shadow: 0 6px 18px rgba(0,0,0,0.18);
  }
  .card--front { top: 50px; background: var(--brand-blue); }
  .card--back  { top: 486px; background: var(--paper); }

  .wordmark {
    position: absolute;
    font-family: "Montserrat", sans-serif;
    font-weight: 700;
    letter-spacing: 1px;
    white-space: nowrap;
    line-height: 1;
  }
  .card--front .wordmark--main {
    left: 0; right: 0; top: 158px;
    text-align: center;
    font-size: 62px;
    color: var(--paper);
  }
  .card--front .wordmark--ghost {
    left: 360px; top: 238px;
    font-size: 70px;
    color: var(--ghost-on-blue);
  }
  .card--back .wordmark--main {
    left: 56px; top: 70px;
    font-size: 58px;
    color: var(--brand-blue);
  }
  .card--back .wordmark--ghost {
    left: 380px; top: 28px;
    font-size: 76px;
    color: var(--ghost-on-white);
  }

  .contact {
    position: absolute;
    left: 0;
    top: 208px;
    padding-left: 56px;
  }
  .contact__bar {
    position: absolute;
    left: 0;
    top: 4px;
    width: 32px;
    height: 54px;
    background: var(--brand-blue);
  }
  .contact__name {
    margin: 0;
    font-family: "Montserrat", sans-serif;
    font-weight: 700;
    font-size: 24px;
    letter-spacing: 0.5px;
    color: var(--brand-blue);
    text-transform: uppercase;
  }
  .contact__role {
    margin: 2px 0 0;
    font-family: "Jost", sans-serif;
    font-size: 20px;
    letter-spacing: 1px;
    color: var(--muted);
  }
  .contact__list {
    list-style: none;
    margin: 22px 0 0;
    padding: 0;
    font-family: "Jost", sans-serif;
    font-size: 21px;
    letter-spacing: 1px;
    color: var(--ink);
  }
  .contact__list li {
    display: flex;
    align-items: center;
    gap: 10px;
    margin-bottom: 4px;
  }
  .contact__icon { width: 20px; height: 20px; flex: none; }

  .address {
    position: absolute;
    right: 48px;
    top: 214px;
    margin: 0;
    text-align: right;
    font-family: "Jost", sans-serif;
    font-style: normal;
    font-size: 20px;
    line-height: 1.35;
    letter-spacing: 1px;
    color: var(--ink);
  }
</style>
</head>
<body>
<main class="sheet">
  <section class="card card--front" aria-label="Business card front">
    <div class="wordmark wordmark--ghost" aria-hidden="true">NORTHVALE</div>
    <div class="wordmark wordmark--main">NORTHVALE</div>
  </section>

  <section class="card card--back" aria-label="Business card back">
    <div class="wordmark wordmark--ghost" aria-hidden="true">NORTHVALE</div>
    <div class="wordmark wordmark--main">NORTHVALE</div>

    <div class="contact">
      <span class="contact__bar"></span>
      <h1 class="contact__name">Dana Whitford</h1>
      <p class="contact__role">Brand Consultant</p>
      <ul class="contact__list">
        <li>
          <svg class="contact__icon" viewBox="0 0 24 24" aria-hidden="true">
            <path fill="#0399d9" d="M6.6 10.8a15 15 0 0 0 6.6 6.6l2.2-2.2a1 1 0 0 1 1-.25 11.4 11.4 0 0 0 3.6.57 1 1 0 0 1 1 1V20a1 1 0 0 1-1 1A17 17 0 0 1 3 4a1 1 0 0 1 1-1h3.5a1 1 0 0 1 1 1c0 1.25.2 2.45.57 3.6a1 1 0 0 1-.25 1z"/>
          </svg>
          (555) 310 4827
        </li>
        <li>
          <svg class="contact__icon" viewBox="0 0 24 24" aria-hidden="true">
            <rect x="2" y="5" width="20" height="14" fill="#0399d9"/>
            <path d="M2 5l10 8 10-8" fill="none" stroke="#ffffff" stroke-width="1.6"/>
          </svg>
          dana@northvale.com
        </li>
      </ul>
    </div>

    <address class="address">
      4580 Linden Avenue<br>
      Ste 210 Fairhill, CA 90000
    </address>
  </section>
</main>
</body>
</html>
```